Rock, Paper Scissors Championship Flyer

We need a dynamic, bold and exciting flyer to promote the following event at our sports center. The event will be primarily focused for adults, but children are welcome to join

Rock, Paper, Scissors Championship - $$$ prizes
Date: June 9th, 2018
Time: 11am-4pm
Fee: $2 to enter, free for spectators
Heats to determine the overall ‘Rock, Paper, Scissors’ champion!
- Cash prizes on offer
- Live music.
- Food and beverage available for purchase

Belvorrow Sports Center, Roselle NJ
908-555-3162
www.belvorrowgrounds.example

Must include our logo (does not have to be huge) and County seal (both attached)

Colors

Designer to choose colors to be used in the design.

Requirements
Must have
• Should be fun and colorful
• The following info and attached logos:
• Rock, Paper, Scissors Championship - $$$ prizes
• Date: June 9th, 2018
• Time: 11am-4pm
• Fee: $2 to enter, free for spectators
• Heats to determine the overall ‘Rock, Paper, Scissors’ champion!
• - Cash prizes on offer
• - Live music.
• - Food and beverage available for purchase
• Belvorrow Sports Center, Roselle NJ
• 908-555-3162
• www.belvorrowgrounds.example
Nice to have
• There are a few inspirational photos attached to give an idea of what we are looking for.

```html
<!DOCTYPE html>
<html lang="en">
<head>
<meta charset="utf-8">
<title>Rock Paper Scissors Championship</title>
<link href="https://fonts.googleapis.com/css2?family=Passion+One:wght@700&family=Teko:wght@500;600&family=Rubik:wght@800&family=Ubuntu+Condensed&display=swap" rel="stylesheet">
<style>
  :root{
    --page:#e9e9ea;
    --sky-top:#6e9fe6;
    --sky-mid:#4f70d6;
    --night:#352ea0;
    --night-deep:#2b2590;
    --pink:#d8345f;
    --teal:#3fcdb6;
    --yellow:#d9d52c;
    --note:#d4d63a;
    --red:#e0263a;
    --ink:#141414;
    --white:#ffffff;
  }
  *{box-sizing:border-box;margin:0;padding:0}
  html,body{width:1200px;height:1190px;overflow:hidden;background:var(--page)}
  .flyer{
    position:absolute;left:169px;top:40px;width:862px;height:1110px;overflow:hidden;
    background:linear-gradient(180deg,var(--sky-top) 0%,var(--sky-mid) 42%,var(--night) 68%,var(--night-deep) 100%);
  }
  .tile{position:absolute}
  .tile--rock{left:-14px;top:30px;width:240px;height:220px;background:var(--pink);transform:rotate(-8deg)}
  .tile--paper{left:226px;top:-6px;width:396px;height:206px;background:var(--teal);transform:rotate(-4deg)}
  .tile--scissors{left:604px;top:84px;width:280px;height:216px;background:var(--yellow);transform:rotate(-6deg)}
  .forest{position:absolute;left:0;top:470px;width:862px;height:300px;
    background:linear-gradient(180deg,rgba(60,70,190,0) 0%,#3c4cc0 30%,#3531a4 100%)}
  .title-blob{position:absolute;left:170px;top:176px;width:536px;height:376px}
  .title{position:absolute;left:170px;top:222px;width:536px;text-align:center;
    font-family:"Passion One",sans-serif;font-weight:700;font-size:118px;line-height:.78;letter-spacing:-1px}
  .title span{display:block}
  .title .rock{color:var(--pink)}
  .title .paper{color:var(--teal)}
  .title .scissors{color:var(--yellow)}
  .championship{position:absolute;left:170px;top:502px;width:536px;text-align:center;
    font-family:"Rubik",sans-serif;font-weight:800;font-size:29px;letter-spacing:5px;color:var(--ink)}
  .when{position:absolute;left:0;top:574px;width:862px;text-align:center;
    font-family:"Teko",sans-serif;font-weight:600;font-size:46px;line-height:1;color:var(--yellow)}
  .where{position:absolute;left:0;top:620px;width:862px;text-align:center;
    font-family:"Teko",sans-serif;font-weight:500;font-size:29px;line-height:1;color:var(--white);letter-spacing:.5px}
  .venue-photo{position:absolute;left:461px;top:700px;width:401px;height:270px;
    background:linear-gradient(160deg,#5a7be0 0%,#3b3fa8 45%,#c98a3e 75%,#2d2a80 100%)}
  .note{position:absolute;left:-10px;top:700px;width:480px;height:226px;background:var(--note);
    transform:rotate(-7deg);padding:20px 20px 0 46px;text-align:center;
    font-family:"Ubuntu Condensed","Arial Narrow",sans-serif;font-size:26px;line-height:1.1;color:var(--ink)}
  .note strong{font-family:"Rubik",sans-serif;font-weight:800;font-size:23px}
  .note .red{color:var(--red)}
  .prize{position:absolute;left:618px;top:614px;width:202px;height:202px;border-radius:50%;background:var(--red);
    display:flex;flex-direction:column;align-items:center;justify-content:center;transform:rotate(-8deg);color:var(--white)}
  .prize .cash{font-family:"Passion One",sans-serif;font-size:96px;line-height:.8}
  .prize .label{font-family:"Rubik",sans-serif;font-weight:800;font-size:30px;letter-spacing:2px}
  .brand{position:absolute;left:30px;top:1010px;width:160px;text-align:center;
    font-family:"Teko",sans-serif;font-weight:500;font-size:26px;line-height:.95;color:var(--white);display:flex;flex-direction:column;align-items:center;gap:6px}
  .brand .dot{width:38px;height:38px;border-radius:50%;background:var(--white)}
  .contact{position:absolute;left:196px;top:1044px;font-family:"Teko",sans-serif;font-weight:600;font-size:30px;line-height:1;color:var(--yellow);white-space:nowrap}
  .contact .phone{margin-right:18px}
  .seal{position:absolute;left:784px;top:1032px;width:52px;height:52px;border-radius:50%;border:3px solid var(--white);opacity:.85}
</style>
</head>
<body>
<main class="flyer">
  <div class="tile tile--rock" role="img" aria-label="Illustrated fist making the rock gesture on a pink tile"></div>
  <div class="tile tile--paper" role="img" aria-label="Illustrated flat hand making the paper gesture on a teal tile"></div>
  <div class="tile tile--scissors" role="img" aria-label="Illustrated hand making the scissors gesture on a yellow tile"></div>

  <div class="forest" role="img" aria-label="Silhouette of a pine forest at dusk"></div>

  <svg class="title-blob" viewBox="0 0 536 376" aria-hidden="true">
    <polygon fill="#ffffff" points="40,58 150,6 300,0 420,20 500,40 522,130 536,250 500,330 380,360 210,376 70,350 14,290 0,170 10,100"/>
  </svg>
  <h1 class="title"><span class="rock">ROCK</span><span class="paper">PAPER</span><span class="scissors">SCISSORS</span></h1>
  <p class="championship">CHAMPIONSHIP</p>

  <p class="when">SATURDAY JUNE 9TH, 2018 11AM-4PM</p>
  <p class="where">BELVORROW SPORTS CENTER, ROSELLE NJ</p>

  <div class="venue-photo" role="img" aria-label="Photo of the sports center building lit at dusk"></div>

  <div class="note">
    $2 to enter, <strong>FREE</strong> for spectators<br>
    <span class="red">Heats to determine the overall<br>‘Rock Paper Scissors’ champion!</span><br>
    Cash prizes on offer. Live music.<br>
    <span class="red">Food and beverage available<br>for purchase.</span>
  </div>

  <div class="prize"><span class="cash">$$$</span><span class="label">PRIZES</span></div>

  <div class="brand"><span class="dot"></span>BELVORROW<br>SPORTS CENTER</div>
  <p class="contact"><span class="phone">908-555-3162</span><span class="web">WWW.BELVORROWGROUNDS.EXAMPLE</span></p>
  <div class="seal" role="img" aria-label="County seal"></div>
</main>
</body>
</html>
```